Packaging design for Organic Beard Care brand - Talon Meadows

This packaging design will be for our beard oil collection which include five different beard oil scents and our signature blend beard oil which is separate from the collection.
There will be two different variants of the box design needed:
Variant 1: White box with Logo and text (Ingredients, Directions, etc).
The words “Handcrafted Premium Beard Oil” will be printed in green foil color. Work this into the design.
Variant 2: Black box with gold foil logo and gold foil text (Ingredients, Directions, etc).
The words “Handcrafted Premium Beard Oil” will be printed in gold foil color. Work this into the design.
Both boxes should have a premium look and feel to it without too much noise.
(Think Brisk deodorant & shampoo brand or Plume teeth whitening brand)
Key callouts will be provided to add to the box designs.
I’ve attached icons, logos, images of the beard oil products and UPC codes that should be used on each box variant.
Please message me if there are more image assets or questions you have about creating the package design.
**Important** - You must create the design on the template file: 30ml-cardboard-box-template-talon-meadows.ai. Any submissions without the design within this template will be passed up/rejected.
Men 21-50
Health & Beauty Cosmetics
- Miso, ASAP Condensed

```html
<!DOCTYPE html>
<html lang="en">
<head>
<meta charset="utf-8">
<title>Talon Meadows – Beard Oil Box Fronts</title>
<link href="https://fonts.googleapis.com/css2?family=Asap+Condensed:wght@400;600;700&family=Dosis:wght@300;400;500&family=Montserrat:wght@700&display=swap" rel="stylesheet">
<style>
  :root{
    --stage:#cfcfcf;
    --box:#ffffff;
    --box-edge:#f1f1f1;
    --ink:#222222;
    --ink-soft:#3a3a3a;
    --grey:#555555;
    --green:#3f8a2c;
    --green-dark:#1f6b1e;
    --green-deep:#2d6f2b;
    --green-light:#aed362;
    --mark:#1c1c1c;
    --ghost:#eef5ea;
  }
  *{box-sizing:border-box;margin:0;padding:0}
  html,body{width:1200px;height:950px;overflow:hidden}
  body{background:var(--stage);position:relative;font-family:"Dosis",sans-serif;color:var(--ink)}

  .box-front{
    position:absolute;top:87px;width:238px;height:696px;
    background:linear-gradient(180deg,var(--box) 0%,var(--box) 70%,var(--box-edge) 100%);
    box-shadow:0 2px 4px rgba(0,0,0,.12);
    overflow:hidden;
  }
  .box-front > *{position:absolute}
  .option-label{
    position:absolute;top:834px;width:238px;text-align:center;
    font-family:"Montserrat",sans-serif;font-weight:700;font-size:20px;color:var(--ink);
  }

  .brand{left:0;width:100%;text-align:center;font-size:14px;color:var(--ink-soft)}
  .brand-dot{left:50%;width:36px;height:36px;margin-left:-18px;border-radius:50%;background:var(--mark)}

  .beard-oil{
    font-family:"Asap Condensed",sans-serif;font-weight:700;line-height:1;
    background:linear-gradient(90deg,var(--green-dark),var(--green) 45%,var(--green-dark));
    -webkit-background-clip:text;background-clip:text;color:transparent;
  }
  .script-line{font-family:"Asap Condensed",sans-serif;font-weight:400;color:var(--green)}
  .small-caps{font-size:13px;color:var(--ink);letter-spacing:.2px}
  .centered{left:0;width:100%;text-align:center}

  /* Option 1 */
  .o1 .kicker{top:124px;left:18px;right:18px;display:flex;align-items:center;gap:6px;font-family:"Asap Condensed",sans-serif;font-size:13px;color:var(--green);letter-spacing:.3px}
  .o1 .kicker::before,.o1 .kicker::after{content:"";flex:1;height:1px;background:var(--green)}
  .o1 .beard-oil{top:144px;font-size:45px}
  .o1 .scent-band{top:210px;left:0;width:100%;height:47px;background:linear-gradient(90deg,#0f5a16,#5fae35 45%,#8fcf55 55%,#0f5a16);color:#fff;font-size:20px;letter-spacing:3px;display:flex;align-items:center;justify-content:center}
  .o1 .ghost-circle{top:318px;left:20px;width:200px;height:190px;border-radius:50%;background:var(--ghost)}

  /* Option 2 */
  .o2 .seal{top:177px;left:15px;width:56px;height:56px;border-radius:50%;background:var(--mark);box-shadow:inset 0 0 0 4px #d9b64a}
  .o2 .script-line{top:256px;left:11px;font-size:15px}
  .o2 .beard-oil{top:269px;left:9px;font-size:31px}
  .o2 .claim{top:303px;left:9px;width:150px;border-top:1px solid var(--ink-soft);border-bottom:1px solid var(--ink-soft);padding:8px 0 6px;line-height:19px}
  .o2 .tagline{top:369px;left:9px}
  .o2 .scent-vertical{top:520px;left:200px;transform:rotate(-90deg);transform-origin:top left;font-size:22px;font-weight:300;letter-spacing:15px;white-space:nowrap;color:var(--ink-soft)}
  .o2 .net{top:578px;left:9px}
  .o2 .band{top:605px;left:0;width:100%;height:26px;background:var(--green-light)}

  /* Front */
  .front .scent-top{top:12px;font-size:21px;letter-spacing:3px;color:var(--ink-soft)}
  .front .stack{top:578px;left:52px;width:310px;transform:rotate(-90deg);transform-origin:top left;text-align:center}
  .front .stack .script-line{display:block;font-size:24px;letter-spacing:.5px;line-height:26px}
  .front .stack .beard-oil{display:block;font-size:76px;letter-spacing:1px;line-height:64px}
  .front .stack .claim{display:block;font-family:"Asap Condensed",sans-serif;font-size:14.5px;line-height:20px;padding-bottom:3px;border-bottom:1px solid var(--ink-soft)}
  .front .tagline{top:598px}
  .front .band{top:625px;left:0;width:100%;height:16px;background:var(--green-deep)}
  .front .net{top:662px}

  /* Option 3 */
  .o3 .tagline{top:24px}
  .o3 .script-line{top:232px;font-size:17px}
  .o3 .beard-oil{top:243px;font-size:47px}
  .o3 .claim{top:295px;left:8px;right:0;border-top:1px solid var(--ink-soft);border-bottom:1px solid var(--ink-soft);padding:7px 0;font-family:"Asap Condensed",sans-serif;font-size:13.5px;text-align:center}
  .o3 .scent{top:525px;font-family:"Asap Condensed",sans-serif;font-size:25px;color:var(--grey)}
  .o3 .band{top:568px;left:0;width:100%;height:26px;background:var(--green-light)}
  .o3 .net{top:614px}
</style>
</head>
<body>

  <section class="box-front o1" style="left:87px">
    <span class="brand-dot" style="top:44px"></span>
    <p class="brand" style="top:88px">Talon Meadows</p>
    <p class="kicker">HANDCRAFTED PREMIUM</p>
    <h2 class="beard-oil centered">BEARD OIL</h2>
    <div class="scent-band">SWEET ALMOND</div>
    <div class="ghost-circle"></div>
    <p class="small-caps centered" style="top:558px;line-height:21px">100% All-Natural &amp; Organic Ingredients<br>None of that artificial stuff!</p>
    <p class="small-caps centered" style="top:624px">net wt. 30ml/1fl.oz.</p>
  </section>
  <p class="option-label" style="left:87px">FRONT OPTION1</p>

  <section class="box-front o2" style="left:361px">
    <span class="seal"></span>
    <p class="script-line">Handcrafted Premium</p>
    <h2 class="beard-oil">BEARD OIL</h2>
    <p class="claim small-caps">100% ALL-NATURAL<br>&amp; ORGANIC INGREDIENTS</p>
    <p class="tagline small-caps">NONE OF THAT ARTIFICIAL STUFF!</p>
    <p class="scent-vertical">SWEET ALMOND</p>
    <p class="net small-caps">net wt. 30ml/1fl.oz.</p>
    <div class="band"></div>
  </section>
  <p class="option-label" style="left:361px">FRONT OPTION2</p>

  <section class="box-front front" style="left:644px">
    <p class="scent-top centered">SWEET ALMOND</p>
    <span class="brand-dot" style="top:106px"></span>
    <p class="brand" style="top:150px">Talon Meadows</p>
    <div class="stack">
      <span class="script-line">HANDCRAFTED PREMIUM</span>
      <span class="beard-oil">BEARD OIL</span>
      <span class="claim">100% ALL-NATURAL &amp; ORGANIC INGREDIENTS</span>
    </div>
    <p class="tagline small-caps centered">NONE OF THAT ARTIFICIAL STUFF!</p>
    <div class="band"></div>
    <p class="net small-caps centered">NET WT. 30ML / 1 FL. OZ.</p>
  </section>
  <p class="option-label" style="left:644px">FRONT</p>

  <section class="box-front o3" style="left:913px">
    <p class="tagline small-caps centered">NONE OF THAT ARTIFICIAL STUFF!</p>
    <span class="brand-dot" style="top:152px"></span>
    <p class="brand" style="top:196px">Talon Meadows</p>
    <p class="script-line centered">Handcrafted Premium</p>
    <h2 class="beard-oil centered">BEARD OIL</h2>
    <p class="claim">100% ALL-NATURAL &amp; ORGANIC INGREDIENTS</p>
    <p class="scent centered">SWEET ALMOND</p>
    <div class="band"></div>
    <p class="net small-caps centered">NET WT. 30ML / 1 FL. OZ.</p>
  </section>
  <p class="option-label" style="left:913px">FRONT OPTION3</p>

</body>
</html>
```